FROSTVIGOR

We need 2 different business card designs for our new company FrostVigor based in Los Angeles,California. Both cards will have front and back designs, There is 2 different cards we need designed. I submitted payment of $90. Please let me know if we need to submit another payment..
We liked this designs and I have attached our fav styles named card 1 and card 2.
Brief info about our company, our main service is the Cryotherpahy Chamber, the many benefits of Cryotherapy include overall wellness, weight loss, athletic recovery and beauty & anti-aging. Explanation on benefits is in pic attached. The final design should communicate wellness.
Wording and colors we want on card:
DESIGN card 1-
Colors: white and blues feel free to experiment (the current colors of the card are pretty good with the look we want. We just want to Logo to flow with the color of the card.
FRONT OF CARD:
FrstVigor logo ( see attached logos in all formats)
Cryotherapy services
Sam Verhallen Owner/Partner
Cell phone icon- 818-555-0192
Office Phone Icon- 805-555-0147
email icon- Sam@frost-vigor.example
www.frost-vigor.example
————————
5912 W MAPLEGROVE PKWY.
WEST LAKE VILLAGE, CA 91300
BACK OF CARD ( you can play with different colors here as well.) Same concept with the blues whites and grey
Health & Wellness
*
Weight Loss
*
Athletic Recovery
*
Beauty & Anti-Aging
-------------------------------------------------
DESIGN Card 2-
On your current card there is water drops. We are trying to get the concept of a cold theme. Maybe snow flakes instead of water drops. See our attached picture with the machine and Ice/snow theme
FRONT OF CARD:
Cryotherapy services
email icon- Info@frost-vigor.example
www.frost-vigor.example
————————
WESTLAKE VILLAGE, CA 91300
BACK OF CARD option 1:
20% off your 1st Whole Body Cryo Package
or
50% off First Whole Body Cryo Session
Discover FrostVigor!
Just 3 Minutes For Total Body CryoTherapy
* first time Guests only. Certain Restrictions Apply (please put this in very small writing on the bottom of the card )
Back Of Card Option 2 ( I need the same exact thing on the front of the card, same color schemes. The only changes we need is to have on the Back.
1 Free Whole Body Cryo Session
Discover FrostVigor!
Certain Restrictions Apply (please put this in very small writing on the bottom of the card )

```html
<!DOCTYPE html>
<html lang="en">
<head>
<meta charset="utf-8">
<title>FrostVigor Business Card</title>
<link rel="stylesheet" href="https://fonts.googleapis.com/css2?family=Open+Sans:ital,wght@0,300;0,400;0,700;1,400&display=swap">
<style>
  :root {
    --page-bg: #e9edf2;
    --front-sky: #2e9edb;
    --front-deep: #1f3fd9;
    --front-deep-dark: #1a2fb0;
    --edge-light: #7fcdf0;
    --back-deep: #0f5db5;
    --back-mid: #1b74cc;
    --wave-light: #6cc6ec;
    --wave-pale: #9edaf4;
    --ice: #37c3ef;
    --silver: #d3dde8;
    --white: #ffffff;
  }
  * { box-sizing: border-box; margin: 0; padding: 0; }
  html, body { width: 1200px; height: 1200px; overflow: hidden; }
  body {
    background: var(--page-bg);
    font-family: "Open Sans", Arial, sans-serif;
    color: var(--white);
    position: relative;
  }
  .card {
    position: absolute;
    left: 150px;
    width: 900px;
    height: 515px;
    overflow: hidden;
    box-shadow: 0 10px 28px rgba(20, 40, 80, .25);
  }
  .card-front { top: 45px; }
  .card-back { top: 630px; }
  .card-art { position: absolute; inset: 0; width: 100%; height: 100%; }

  .brand {
    position: absolute;
    display: flex;
    align-items: center;
    gap: 14px;
    font-weight: 700;
    color: var(--silver);
    letter-spacing: .5px;
  }
  .brand-dot { border-radius: 50%; background: var(--ice); flex: none; }
  .card-front .brand { left: 50px; top: 222px; font-size: 50px; }
  .card-front .brand-dot { width: 34px; height: 34px; }
  .card-back .brand { left: 0; right: 0; justify-content: center; top: 95px; font-size: 68px; }
  .card-back .brand-dot { width: 44px; height: 44px; }

  .service-title {
    position: absolute; right: 38px; top: 50px;
    font-size: 42px; font-weight: 700; line-height: 1;
  }
  .person-name {
    position: absolute; right: 42px; top: 106px;
    font-size: 40px; font-weight: 300; line-height: 1;
  }
  .person-role {
    position: absolute; right: 44px; top: 156px;
    font-size: 18px; font-style: italic;
  }
  .contact-list {
    position: absolute; left: 545px; top: 212px;
    list-style: none;
  }
  .contact-list li {
    display: flex; align-items: center; gap: 16px;
    height: 42px; font-size: 22px;
  }
  .contact-icon { width: 32px; height: 32px; flex: none; }
  .divider {
    position: absolute; left: 495px; right: 22px; top: 392px;
    height: 3px; background: var(--white);
  }
  .address {
    position: absolute; left: 560px; top: 408px;
    font-size: 21px; line-height: 1.45;
  }

  .offer {
    position: absolute; left: 58px; top: 318px;
    font-weight: 700; font-size: 30px; line-height: 1.3;
    text-shadow: 0 1px 3px rgba(0, 40, 90, .35);
  }
  .offer-discover { text-decoration: underline; text-decoration-thickness: 2px; }
  .fine-print {
    position: absolute; right: 28px; bottom: 16px;
    font-size: 11px; font-weight: 700;
  }
</style>
</head>
<body>

<section class="card card-front">
  <svg class="card-art" viewBox="0 0 900 515" role="img" aria-label="Snowy blue background with soft bokeh and faint frost crystals">
    <defs>
      <radialGradient id="deepField" cx="35%" cy="45%" r="70%">
        <stop offset="0" stop-color="#2e4ff0"/>
        <stop offset="1" stop-color="var(--front-deep-dark)"/>
      </radialGradient>
    </defs>
    <rect width="900" height="515" fill="var(--front-sky)"/>
    <path d="M0 0 H365 C335 45 360 100 415 118 C480 145 505 195 515 245 C525 290 505 345 480 385 C445 425 470 470 450 515 H0 Z" fill="var(--edge-light)"/>
    <path d="M0 0 H350 C320 45 345 100 400 118 C465 145 490 195 500 245 C510 290 490 345 465 385 C430 425 455 470 435 515 H0 Z" fill="var(--white)"/>
    <path d="M0 0 H338 C308 45 333 100 388 118 C453 145 478 195 488 245 C498 290 478 345 453 385 C418 425 443 470 423 515 H0 Z" fill="url(#deepField)"/>
  </svg>

  <div class="brand"><span class="brand-dot"></span>FrostVigor</div>

  <div class="service-title">Cryotherapy services</div>
  <div class="person-name">Sam Verhallen</div>
  <div class="person-role">Owner/Partner</div>

  <ul class="contact-list">
    <li>
      <svg class="contact-icon" viewBox="0 0 32 32" aria-hidden="true"><rect width="32" height="32" rx="6" fill="#fff"/><rect x="10" y="5" width="12" height="22" rx="2" fill="none" stroke="var(--front-sky)" stroke-width="2.5"/><rect x="13" y="9" width="6" height="6" fill="var(--front-sky)"/></svg>
      818-555-0192
    </li>
    <li>
      <svg class="contact-icon" viewBox="0 0 32 32" aria-hidden="true"><rect width="32" height="32" rx="6" fill="#fff"/><path d="M6 13 C10 7 22 7 26 13 L22 15 L20 12 H12 L10 15 Z" fill="var(--front-sky)"/><rect x="9" y="16" width="14" height="9" rx="2" fill="var(--front-sky)"/><circle cx="16" cy="20.5" r="2.3" fill="#fff"/></svg>
      805-555-0147
    </li>
    <li>
      <svg class="contact-icon" viewBox="0 0 32 32" aria-hidden="true"><rect width="32" height="32" rx="6" fill="#fff"/><rect x="6" y="9" width="20" height="14" fill="none" stroke="var(--front-sky)" stroke-width="2"/><path d="M6 9 L16 17 L26 9" fill="none" stroke="var(--front-sky)" stroke-width="2"/></svg>
      Sam@frost-vigor.example
    </li>
    <li>
      <svg class="contact-icon" viewBox="0 0 32 32" aria-hidden="true"><rect width="32" height="32" rx="6" fill="#fff"/><circle cx="16" cy="16" r="10" fill="none" stroke="var(--front-sky)" stroke-width="2"/><ellipse cx="16" cy="16" rx="4.5" ry="10" fill="none" stroke="var(--front-sky)" stroke-width="1.6"/><path d="M6 16 H26 M8 11 H24 M8 21 H24" stroke="var(--front-sky)" stroke-width="1.6"/></svg>
      www.frost-vigor.example
    </li>
  </ul>

  <div class="divider"></div>
  <div class="address">5912 W MAPLEGROVE PKWY.<br>WEST LAKE VILLAGE, CA 91300</div>
</section>

<section class="card card-back">
  <svg class="card-art" viewBox="0 0 900 515" role="img" aria-label="Deep blue snowy sky with bokeh over a pale icy wave with frost crystals">
    <defs>
      <linearGradient id="backSky" x1="0" y1="0" x2="0" y2="1">
        <stop offset="0" stop-color="var(--back-mid)"/>
        <stop offset="1" stop-color="var(--back-deep)"/>
      </linearGradient>
      <linearGradient id="iceWave" x1="0" y1="0" x2="1" y2="1">
        <stop offset="0" stop-color="var(--wave-pale)"/>
        <stop offset="1" stop-color="var(--wave-light)"/>
      </linearGradient>
    </defs>
    <rect width="900" height="515" fill="url(#backSky)"/>
    <path d="M0 300 C120 250 230 250 360 300 C520 365 640 400 900 320 V515 H0 Z" fill="url(#iceWave)"/>
  </svg>

  <div class="brand"><span class="brand-dot"></span>FrostVigor</div>

  <div class="offer">
    <div>Free Whole Body Cryo Session</div>
    <div class="offer-discover">Discover FrostVigor!</div>
    <div>Just 3 Minutes For Total Body CryoTherapy</div>
  </div>

  <div class="fine-print">*Certain Restrictions Apply</div>
</section>

</body>
</html>
```